Financial Advisor Resource Firm needs business card design

Need business card design for company in Omaha NE called Tallowbrook Partners. We provide resources to financial advisors....workshop programs, retirement analysis, and insurance planning. I would like to see designs that use grays, greens, black, and white colors. The final design should communicate 'collaboration' and be simple yet attractive to financial planning clients. I will attached our logo and another picture of a puzzle piece coming together. I would like the incorporate the puzzle picture somehow, maybe on the back somehow, with color or just the gray scale....OR, the picture be the front of the card with 'Tallowbrook' definition on it (see upload) and then company logo, employee name, title, address on the back (see ppt uploaded). The following disclosure needs to be included somewhere- Advisory services offered through Marlowe Ridge Advisors, LLC.
Updates

I uploaded a svg and ai file of the logo

Target Market(s)

Financial planning clients and financial advisors....so pretty diverse age range of about 40-70.

Industry/Entity Type

Financial Planning

Contact Information for Business Card

Dennis K. Holloway, MBA
Founder/President
5727 E. Larkspur Avenue
Suite 418
Omaha, NE 68297
Phone- (402) 555-0147
Cell- (402) 555-0183
Fax- (402) 555-0129
email- dennis@tallowbrookgroup.example
web address- www.tallowbrookgroup.example

Colors
1b1b1b
474747
d3d3d3
ffffff
9bcb3c
abd036

Requirements
Must have
• Must include logo provided, must be 2 sided, and must have disclosure...all of these items listed in project description

```html
<!DOCTYPE html>
<html lang="en">
<head>
<meta charset="utf-8">
<title>Tallowbrook Partners — Business Cards</title>
<link rel="stylesheet" href="https://fonts.googleapis.com/css2?family=Cormorant+SC:wght@500;600&display=swap">
<style>
  :root {
    --stage: #c4d2d6;
    --ink: #1b1b1b;
    --ink-soft: #474747;
    --paper: #ffffff;
    --mist: #d3d3d3;
    --lime: #7ff22b;
    --lime-glass: rgba(127, 242, 43, 0.82);
    --photo-light: #9a9a9a;
    --photo-dark: #2a2a2a;
  }
  * { box-sizing: border-box; margin: 0; padding: 0; }
  html, body { width: 1200px; height: 753px; overflow: hidden; }
  body {
    background: var(--stage);
    font-family: "Cormorant SC", "Times New Roman", serif;
    color: var(--ink);
    position: relative;
  }
  .card {
    position: absolute;
    width: 408px;
    height: 245px;
    overflow: hidden;
    background: var(--paper);
  }
  .card--front-a { left: 165px; top: 110px; }
  .card--back-a  { left: 607px; top: 110px; }
  .card--front-b { left: 165px; top: 410px; }
  .card--back-b  { left: 607px; top: 410px; }

  .wordmark {
    position: absolute;
    display: flex;
    align-items: center;
    gap: 7px;
    font-size: 19px;
    font-weight: 600;
    letter-spacing: 0.4px;
    line-height: 1;
    white-space: nowrap;
  }
  .wordmark__dot {
    width: 11px; height: 11px; border-radius: 50%;
    background: var(--lime);
  }
  .wordmark--dark { color: var(--ink); }
  .wordmark--light { color: var(--paper); }

  .person__name { font-size: 17px; font-weight: 600; line-height: 1; }
  .person__title { font-size: 16px; font-weight: 500; line-height: 1; margin-top: 4px; }

  .contact { font-size: 12px; font-weight: 500; line-height: 14px; color: var(--ink); }
  .contact--small { font-size: 9px; line-height: 12px; }

  /* Front A */
  .card--front-a .wordmark { left: 0; right: 0; top: 44px; justify-content: center; }
  .card--front-a .person { position: absolute; left: 0; right: 0; top: 101px; text-align: center; }
  .band {
    position: absolute; left: 0; right: 0; top: 148px; height: 57px;
    background: var(--lime);
  }
  .card--front-a .band .contact { text-align: center; padding-top: 15px; }
  .card--front-a .footer-line { position: absolute; left: 0; right: 0; top: 218px; text-align: center; }

  /* Photo backs */
  .photo {
    position: absolute; inset: 0;
    background:
      radial-gradient(ellipse at 70% 75%, #bdbdbd 0%, rgba(189,189,189,0) 45%),
      linear-gradient(160deg, var(--photo-light) 0%, #6e6e6e 45%, var(--photo-dark) 100%);
  }
  .card--back-a .band, .card--back-b .band { background: var(--lime-glass); }
  .card--back-a .wordmark, .card--back-b .wordmark { left: 0; right: 0; top: 108px; justify-content: center; }
  .tagline {
    position: absolute; left: 0; width: 408px; text-align: center;
    font-size: 11px; line-height: 14px; letter-spacing: 0.4px;
  }
  .card--back-a .tagline { top: 166px; color: var(--ink-soft); }
  .card--back-b .tagline { top: 166px; color: var(--paper); }
  .disclosure {
    position: absolute; left: 0; width: 408px; top: 207px; text-align: center;
    font-size: 11px; color: var(--mist); letter-spacing: 0.3px;
  }
  .tab { position: absolute; top: 148px; width: 22px; height: 57px; background: var(--lime); }
  .card--back-b .tab { left: 388px; width: 20px; }

  /* Front B */
  .card--front-b .wordmark { left: 35px; top: 44px; }
  .card--front-b .person { position: absolute; left: 32px; top: 101px; }
  .card--front-b .tab { left: 0; }
  .card--front-b .address { position: absolute; left: 31px; top: 161px; }
  .card--front-b .footer-lines { position: absolute; left: 31px; top: 207px; }
  .ornament-area {
    position: absolute; left: 262px; top: 0; width: 146px; height: 150px;
    background: radial-gradient(ellipse at 60% 45%, rgba(200,200,200,0.55) 0%, rgba(211,211,211,0.25) 50%, rgba(255,255,255,0) 75%);
  }
</style>
</head>
<body>

<section class="card card--front-a" aria-label="Card front, version one">
  <div class="wordmark wordmark--dark"><span class="wordmark__dot"></span>Tallowbrook Partners</div>
  <div class="person">
    <p class="person__name">Dennis K. Holloway, MBA</p>
    <p class="person__title">Founder/President</p>
  </div>
  <div class="band">
    <p class="contact">5727 E. Larkspur Avenue, Suite 418, Omaha, NE 68297<br>
    Phone: (402) 555-0147 | Cell: (402) 555-0183 | Fax: (402) 555-0129</p>
  </div>
  <p class="contact contact--small footer-line">E-mail: dennis@tallowbrookgroup.example | Web: www.tallowbrookgroup.example</p>
</section>

<section class="card card--back-a" aria-label="Card back, version one">
  <div class="photo" role="img" aria-label="Grayscale photograph of hands joining puzzle pieces together"></div>
  <div class="wordmark wordmark--light"><span class="wordmark__dot"></span>Tallowbrook Partners</div>
  <div class="band"></div>
  <p class="tagline">To come together and unite in<br>common interest and focus</p>
</section>

<section class="card card--front-b" aria-label="Card front, version two">
  <div class="ornament-area" role="img" aria-label="Faint gray decorative ornament"></div>
  <div class="wordmark wordmark--dark"><span class="wordmark__dot"></span>Tallowbrook Partners</div>
  <div class="person">
    <p class="person__name">Dennis K. Holloway, MBA</p>
    <p class="person__title">Founder/President</p>
  </div>
  <div class="tab"></div>
  <p class="contact address">5727 E. Larkspur Avenue, Suite 418, Omaha, NE 68297<br>
  Phone: (402) 555-0147 | Cell: (402) 555-0183 | Fax: (402) 555-0129</p>
  <p class="contact contact--small footer-lines">E-mail: dennis@tallowbrookgroup.example<br>Web: www.tallowbrookgroup.example</p>
</section>

<section class="card card--back-b" aria-label="Card back, version two">
  <div class="photo" role="img" aria-label="Grayscale photograph of hands joining puzzle pieces together"></div>
  <div class="wordmark wordmark--light"><span class="wordmark__dot"></span>Tallowbrook Partners</div>
  <p class="tagline">To come together and unite in<br>common interest and focus</p>
  <p class="disclosure">Marlowe Ridge Advisors, LLC</p>
  <div class="tab"></div>
</section>

</body>
</html>
```